Brivane - Business Cards for a new venture

create business card for a startup classified business dealing in construction materials, the cards need to have a professional look but modern, more serious than playful, one of the samples must include the official font (attached), please explore using the official colors in the company's logo

Target Market(s)

Energy sector

Contact Information for Business Card

Font styles to use
Other font styles liked:
• suissnord

Requirements
Must have
• corporate colors (in logo attached)
Nice to have
• Official font (in one of the samples) font is : suissnord
Should not have
• Cartoonish look

```html
<!DOCTYPE html>
<html lang="en">
<head>
<meta charset="utf-8">
<title>Brivane Business Cards</title>
<link rel="stylesheet" href="https://fonts.googleapis.com/css2?family=Orbitron:wght@400;500&display=swap">
<style>
  :root {
    --backdrop: #2a2a2a;
    --card-white: #ffffff;
    --brand-navy: #1d4a73;
    --brand-blue: #0f426d;
    --brand-gray: #8d8d8d;
    --text-gray: #5f5f5f;
    --mark-white: #ffffff;
  }
  html, body {
    margin: 0;
    padding: 0;
    width: 1200px;
    height: 960px;
    overflow: hidden;
    background: var(--backdrop);
  }
  .canvas {
    position: relative;
    width: 1200px;
    height: 960px;
    font-family: "Orbitron", sans-serif;
  }
  .card {
    position: absolute;
    width: 600px;
    height: 342px;
    box-shadow: 2px 3px 6px rgba(0, 0, 0, 0.45);
  }
  .card-front {
    left: 302px;
    top: 119px;
    background: var(--card-white);
  }
  .card-back {
    left: 299px;
    top: 498px;
    background: var(--brand-blue);
  }
  .front-brand {
    position: absolute;
    right: 50px;
    top: 180px;
    transform: translateY(-180px);
    margin-top: 74px;
    display: flex;
    align-items: center;
    gap: 12px;
    color: var(--brand-navy);
    font-size: 30px;
    font-weight: 500;
    letter-spacing: 4px;
    text-transform: uppercase;
  }
  .brand-square {
    width: 18px;
    height: 18px;
    background: var(--brand-navy);
  }
  .holder-name {
    position: absolute;
    left: 33px;
    top: 210px;
    margin: 0;
    color: var(--brand-navy);
    font-size: 23px;
    font-weight: 500;
    letter-spacing: 1.5px;
    text-transform: uppercase;
  }
  .holder-title {
    position: absolute;
    left: 34px;
    top: 237px;
    margin: 0;
    color: var(--brand-gray);
    font-size: 13.5px;
    letter-spacing: 1.5px;
    text-transform: uppercase;
  }
  .divider {
    position: absolute;
    left: 33px;
    top: 263px;
    width: 518px;
    height: 1.5px;
    background: var(--brand-navy);
  }
  .contact {
    position: absolute;
    left: 34px;
    top: 276px;
    margin: 0;
    color: var(--text-gray);
    font-size: 10.5px;
    line-height: 12.5px;
    letter-spacing: 0.8px;
    font-style: normal;
  }
  .back-square {
    position: absolute;
    left: 286px;
    top: 130px;
    width: 28px;
    height: 28px;
    background: var(--mark-white);
  }
  .back-brand {
    position: absolute;
    left: 0;
    width: 600px;
    top: 230px;
    text-align: center;
    color: var(--brand-gray);
    font-size: 31px;
    font-weight: 400;
    letter-spacing: 5px;
    text-transform: uppercase;
  }
</style>
</head>
<body>
<main class="canvas">
  <section class="card card-front" aria-label="Business card front">
    <div class="front-brand"><span class="brand-square"></span>Brivane</div>
    <h1 class="holder-name">Elias Varden</h1>
    <p class="holder-title">CEO/Founder</p>
    <div class="divider"></div>
    <address class="contact">
      4120 Harbor Ridge Road, Kelso, Northland 58210<br>
      Office: 555 210 4817 | Mobile: 555 732 0946<br>
      elias@brivane.com | www.brivane.com
    </address>
  </section>

  <section class="card card-back" aria-label="Business card back">
    <span class="back-square"></span>
    <div class="back-brand">Brivane</div>
  </section>
</main>
</body>
</html>
```